standardize print collateral

we need help standardizing all print collateral and website. top priorities:

1. standardized case studies template
2. standardized marketing slicks template
3. standardized powerpoint template
Updates

Project Deadline Extended
Reason: We are extending the project to allow current design submissions to be tweaked while providing the opportunity for new designs to be submitted. We will need all 3 collateral designs submitted to make a final decision. Please note, these 3 designs should all look different, needless to say they should all compliment eachother. As for some direction, the powerpoint main color should not be yellow since yellow does not show up the same shade on any screen. The case study and marketing slicks will be printed and often sit next to our competitors marketing material - think high end product, technology, revolutionary, edgy, professional. The designs should compliment eachother and feel like the Brightfern Metrics brand (which you are determining) and should stand out professionally. We are open to introducing new colors into our brand, the only thing that must remain the same is our logo. Have fun, make it edgy, and keep it professional. Looking forward to seeing what you submit!

Target Market(s)

Property Casualty Insurance Companies: Executive level wording with actuarial credibility

Industry/Entity Type

Marketing

Requirements
Must have
• professional layout for existing collateral and 2-page marketing slicks. style guide/colors can be transferred to powerpoint. logo must stay; everything else (i.e. color, font, layout/structure etc.) is flexible. The three components should not looks the same, they should only compliment eachother.
Nice to have
• we are revolutionizing a conservative industry, so adequate level of edgy/advanced technology/impactful feel to layout
Should not have
• no need to stay within color constraints of yellow, but need to appropriately work well with the eagle head logo

```html
<!DOCTYPE html>
<html lang="en">
<head>
<meta charset="utf-8">
<title>Rapid Portfolio Analysis – Brightfern Metrics</title>
<link rel="stylesheet" href="https://fonts.googleapis.com/css2?family=Barlow:wght@400;500;600;700&family=Barlow+Condensed:wght@500;600;700&display=swap">
<style>
:root{
  --navy:#1c4d78;
  --navy-deep:#173f63;
  --teal:#2b8bb8;
  --teal-light:#45a9d3;
  --sky:#dcebf4;
  --ink:#3c3c3c;
  --muted:#5d6368;
  --rule:#8fc2de;
  --paper:#ffffff;
  --backdrop:#e9ecef;
  --footer:#e4ecf1;
  --grid:#c9d3da;
}
*{margin:0;padding:0;box-sizing:border-box}
html,body{width:1200px;height:777px;overflow:hidden}
body{background:var(--backdrop);font-family:"Barlow",Arial,sans-serif;color:var(--ink);position:relative}
.page{position:absolute;top:18px;width:560px;height:740px;background:var(--paper);overflow:hidden;box-shadow:0 2px 8px rgba(0,0,0,.18)}
.page--front{left:30px}
.page--back{left:610px}

/* Front page */
.title{position:absolute;left:28px;top:24px;font-family:"Barlow Condensed",Arial,sans-serif;font-weight:600;font-size:36px;line-height:34px;letter-spacing:.5px;color:var(--navy)}
.title span{display:block;color:var(--teal-light)}
.subtitle{position:absolute;left:28px;top:98px;font-family:"Barlow Condensed",Arial,sans-serif;font-size:15px;letter-spacing:.6px;color:var(--navy);font-weight:500}
.subtitle b{font-weight:700}
.hero-art{position:absolute;left:0;top:118px;width:345px;height:262px;background:linear-gradient(160deg,#f4f7fa 0%,#cfe0ec 40%,#7fb3d6 70%,#c9a96a 100%)}
.intro-panel{position:absolute;left:345px;top:0;width:215px;height:405px;background:linear-gradient(180deg,#1f5a86 0%,var(--teal) 55%,#1e6f9e 100%)}
.intro-panel p{position:absolute;left:18px;top:142px;width:185px;font-size:10.2px;line-height:13.2px;color:#fff;font-weight:500}
.how-band{position:absolute;left:0;top:380px;width:240px;height:26px;background:var(--navy);color:#fff;font-family:"Barlow Condensed",Arial,sans-serif;font-size:17px;letter-spacing:.5px;padding:3px 0 0 26px}
.steps{position:absolute;left:26px;top:420px;width:510px;display:flex;gap:10px}
.step{flex:1;padding-right:8px}
.step + .step{border-left:1.5px dashed var(--teal-light);padding-left:10px}
.step h3{font-family:"Barlow Condensed",Arial,sans-serif;font-size:13px;color:var(--teal);letter-spacing:.4px;line-height:13px}
.step h4{font-size:10.5px;color:var(--navy);font-weight:700;line-height:12px;margin-bottom:5px}
.step p{font-size:8.6px;line-height:11.2px;color:var(--muted)}
.report-band{position:absolute;left:0;top:598px;width:560px;height:142px;background:var(--navy-deep)}
.report-band h2{position:absolute;left:26px;top:14px;width:490px;height:22px;background:var(--teal);color:#fff;font-family:"Barlow Condensed",Arial,sans-serif;font-size:13.5px;font-weight:600;letter-spacing:.5px;padding:3px 0 0 14px}
.report-band p{position:absolute;left:40px;top:50px;width:490px;font-size:9px;line-height:12px;color:#e6eef5}

/* Back page */
.top-band{position:absolute;left:0;top:0;width:560px;height:112px;background:linear-gradient(120deg,#2b7fb0 0%,#1c4d78 60%,#3a98c5 100%)}
.monitor-card{position:absolute;top:38px;width:246px;height:168px;background:#fff;box-shadow:0 2px 6px rgba(0,0,0,.25);padding:10px 10px 0}
.monitor-card--portfolio{left:22px}
.monitor-card--distribution{left:292px}
.monitor-card h3{font-family:"Barlow Condensed",Arial,sans-serif;font-size:11px;font-weight:700;color:var(--navy);letter-spacing:.5px;margin-bottom:5px}
.monitor-card svg{display:block}
.monitor-card p{font-size:8px;line-height:10px;color:var(--muted);margin-top:5px}
.headline{position:absolute;left:30px;top:220px;width:500px;text-align:center;font-size:14.5px;line-height:18px;font-weight:700;color:#4b4f53}
.section-head{position:absolute;width:244px;font-family:"Barlow Condensed",Arial,sans-serif;font-size:11.5px;font-weight:700;color:var(--navy);letter-spacing:.5px;border-bottom:3px solid var(--rule);padding-bottom:2px}
.chart{position:absolute}
.chart-note{position:absolute;width:240px;font-size:8.6px;line-height:10.8px;color:var(--muted)}
.exposure-note{position:absolute;left:28px;top:484px;width:506px;font-size:8.8px;line-height:11px;color:var(--muted)}
.footer{position:absolute;left:0;top:650px;width:560px;height:90px;background:var(--footer);border-top:3px solid var(--rule)}
.footer-about{position:absolute;left:28px;top:16px;width:230px;font-size:8.2px;line-height:10.6px;color:var(--muted)}
.footer-about b{color:var(--navy)}
.brand{position:absolute;left:270px;top:30px;display:flex;align-items:center;gap:6px;font-size:13px;font-weight:700;color:var(--navy)}
.brand i{display:block;width:14px;height:14px;border-radius:50%;background:var(--teal)}
.contact{position:absolute;left:385px;top:14px;width:160px;text-align:right;font-size:8.6px;line-height:11.2px;color:var(--navy)}
.contact strong{font-size:9.5px}
</style>
</head>
<body>

<section class="page page--front">
  <h1 class="title">RAPID PORTFOLIO <span>ANALYSIS</span></h1>
  <p class="subtitle">WINNING AGAINST <b>ADVERSE SELECTION</b></p>

  <div class="hero-art" role="img" aria-label="Illustration of a blue arrow rising above golden 3D bar columns"></div>

  <div class="intro-panel">
    <p>The property and casualty market is over-supplied with excess capacity, and current pricing methods are inconsistent and outdated. This leads to a considerable level of adverse selection within nearly every portfolio. Almost every insurer is attracting customers who are underpriced and losing business where they are overpriced. This invisible effect only surfaces after evidence of slowly deteriorating portfolio loss ratios, resulting in premium increases across the portfolio. These across-the-board premium increases exacerbate the problem by overpricing the most profitable customers and driving them into the arms of competitors.</p>
  </div>

  <div class="how-band">HOW DOES IT WORK?</div>

  <div class="steps">
    <article class="step">
      <h3>DETECTION</h3>
      <h4>Is the portfolio priced correctly?</h4>
      <p>Quillon employs a regression method based on a technological breakthrough. It exposes pricing imbalances by commonly employed rating method including the GLM. These pricing imbalances are the major drivers of adverse selection.</p>
    </article>
    <article class="step">
      <h3>MEASUREMENT</h3>
      <h4>How is the portfolio trending?</h4>
      <p>Quillon scores the two most important attributes of the portfolio: the adequacy of rates and the quality of the business on a progressive basis. In addition, Quillon projects the financial outcome of business as it is written with startling accuracy. Insurers are able to know significantly in advance of trends in their business.</p>
    </article>
    <article class="step">
      <h3>CORRECTION</h3>
      <h4>How to address the issues?</h4>
      <p>Quillon provides an array of options for addressing any deterioration in the portfolio. These options range from specifically designed rate adjustments and underwriting strategies, to simple distribution management sales and profitability strategies.</p>
    </article>
  </div>

  <div class="report-band">
    <h2>LET BRIGHTFERN METRICS BUILD YOUR PORTFOLIO ANALYSIS REPORT</h2>
    <p>The report details your portfolio trends and identifies future unseen problems before they occur. The insight provided in the report exhibits what is actually going on in your portfolio. This likely includes adverse selection, impact of price changes with unintended consequences, and the emerging trends in the composition of the book. The analysis results not only reveal past trends, but also predict future impact.</p>
  </div>
</section>

<section class="page page--back">
  <div class="top-band"></div>

  <div class="monitor-card monitor-card--portfolio">
    <h3>PORTFOLIO MONITORING</h3>
    <svg width="226" height="108" viewBox="0 0 226 108" role="img" aria-label="Portfolio monitoring data table">
      <rect x="0" y="0" width="226" height="12" fill="#dfe7ee"/>
      <g stroke="#d3dbe2" stroke-width="0.6">
        <line x1="0" y1="24" x2="226" y2="24"/><line x1="0" y1="36" x2="226" y2="36"/><line x1="0" y1="48" x2="226" y2="48"/><line x1="0" y1="60" x2="226" y2="60"/><line x1="0" y1="72" x2="226" y2="72"/><line x1="0" y1="84" x2="226" y2="84"/><line x1="0" y1="96" x2="226" y2="96"/>
        <line x1="28" y1="0" x2="28" y2="108"/><line x1="62" y1="0" x2="62" y2="108"/><line x1="96" y1="0" x2="96" y2="108"/><line x1="124" y1="0" x2="124" y2="108"/><line x1="150" y1="0" x2="150" y2="108"/><line x1="176" y1="0" x2="176" y2="108"/><line x1="200" y1="0" x2="200" y2="108"/>
      </g>
      <rect x="150" y="12" width="26" height="36" fill="#e07a6a" opacity=".8"/>
      <rect x="150" y="48" width="26" height="24" fill="#f2d36b" opacity=".8"/>
      <rect x="150" y="72" width="26" height="36" fill="#8cc97a" opacity=".8"/>
      <rect x="0" y="96" width="226" height="12" fill="#eef2f5"/>
    </svg>
    <p>Predict the future loss ratio of the business being written – both renewals and new business</p>
  </div>

  <div class="monitor-card monitor-card--distribution">
    <h3>DISTRIBUTION MONITORING</h3>
    <svg width="226" height="108" viewBox="0 0 226 108" role="img" aria-label="Distribution monitoring heat table">
      <rect x="0" y="0" width="226" height="14" fill="#4f9a3f"/>
      <rect x="60" y="3" width="70" height="8" fill="#e3c23a"/>
      <g>
        <rect x="40" y="20" width="30" height="8" fill="#d94a3a"/><rect x="75" y="20" width="30" height="8" fill="#79b94f"/><rect x="110" y="20" width="30" height="8" fill="#79b94f"/>
        <rect x="40" y="34" width="30" height="8" fill="#79b94f"/><rect x="75" y="34" width="30" height="8" fill="#e3c23a"/><rect x="110" y="34" width="30" height="8" fill="#d94a3a"/>
        <rect x="40" y="48" width="30" height="8" fill="#e3c23a"/><rect x="75" y="48" width="30" height="8" fill="#79b94f"/><rect x="110" y="48" width="30" height="8" fill="#79b94f"/>
        <rect x="40" y="62" width="30" height="8" fill="#79b94f"/><rect x="75" y="62" width="30" height="8" fill="#d94a3a"/><rect x="110" y="62" width="30" height="8" fill="#e3c23a"/>
        <rect x="40" y="76" width="30" height="8" fill="#d94a3a"/><rect x="75" y="76" width="30" height="8" fill="#79b94f"/><rect x="110" y="76" width="30" height="8" fill="#79b94f"/>
        <rect x="40" y="90" width="30" height="8" fill="#79b94f"/><rect x="75" y="90" width="30" height="8" fill="#e3c23a"/><rect x="110" y="90" width="30" height="8" fill="#79b94f"/>
      </g>
      <g fill="#9fc0d6">
        <rect x="160" y="20" width="50" height="6"/><rect x="160" y="34" width="38" height="6"/><rect x="160" y="48" width="44" height="6"/><rect x="160" y="62" width="30" height="6"/><rect x="160" y="76" width="52" height="6"/><rect x="160" y="90" width="26" height="6"/>
      </g>
      <g fill="#c4ccd3"><rect x="4" y="20" width="28" height="6"/><rect x="4" y="34" width="28" height="6"/><rect x="4" y="48" width="28" height="6"/><rect x="4" y="62" width="28" height="6"/><rect x="4" y="76" width="28" height="6"/><rect x="4" y="90" width="28" height="6"/></g>
    </svg>
    <p>Constantly track the quality and performance of individual distribution outlets based on the underwriting score of each policy</p>
  </div>

  <h2 class="headline">Quillon detects, measures and presents actionable options to correct the insurance company effects of adverse selection within any P&amp;C portfolio.</h2>

  <h3 class="section-head" style="left:28px;top:268px">UNDERWRITING SCORE</h3>
  <svg class="chart" style="left:22px;top:288px" width="250" height="128" viewBox="0 0 250 128">
    <g font-family="Barlow,Arial,sans-serif" font-size="6.5" fill="#555">
      <text x="26" y="12" text-anchor="end">80%</text><text x="26" y="26" text-anchor="end">70%</text><text x="26" y="40" text-anchor="end">60%</text><text x="26" y="54" text-anchor="end">50%</text><text x="26" y="68" text-anchor="end">40%</text><text x="26" y="82" text-anchor="end">30%</text><text x="26" y="96" text-anchor="end">20%</text><text x="26" y="110" text-anchor="end">10%</text>
      <text x="8" y="70" transform="rotate(-90 8 70)" text-anchor="middle" font-weight="600" fill="#2b8bb8">Loss Ratio</text>
      <text x="47" y="120" text-anchor="middle">0-94</text><text x="79" y="120" text-anchor="middle">95-249</text><text x="111" y="120" text-anchor="middle">250-499</text><text x="143" y="120" text-anchor="middle">500-749</text><text x="175" y="120" text-anchor="middle">750-899</text><text x="207" y="120" text-anchor="middle">900-1000</text>
      <text x="127" y="128" text-anchor="middle" font-weight="600" fill="#2b8bb8">Score Tier</text>
    </g>
    <line x1="30" y1="112" x2="235" y2="112" stroke="#888" stroke-width=".7"/>
    <g fill="#2b8bb8">
      <rect x="40" y="28" width="14" height="84"/><rect x="72" y="54" width="14" height="58"/><rect x="104" y="74" width="14" height="38"/><rect x="136" y="77" width="14" height="35"/><rect x="168" y="88" width="14" height="24"/><rect x="200" y="94" width="14" height="18"/>
    </g>
  </svg>
  <p class="chart-note" style="left:28px;top:421px">Discover the pricing imbalances within the portfolio. These imbalances are the main driver of the adverse selection.</p>

  <h3 class="section-head" style="left:290px;top:268px">TREND AND LOSS RATIO</h3>
  <svg class="chart" style="left:286px;top:288px" width="250" height="128" viewBox="0 0 250 128">
    <g font-family="Barlow,Arial,sans-serif" font-size="6.5" fill="#555">
      <text x="30" y="10" text-anchor="end">60%</text><text x="30" y="34" text-anchor="end">40%</text><text x="30" y="58" text-anchor="end">20%</text><text x="30" y="82" text-anchor="end">0%</text><text x="30" y="106" text-anchor="end">-20%</text>
      <text x="10" y="60" transform="rotate(-90 10 60)" text-anchor="middle" font-weight="600" fill="#2b8bb8">Loss Ratio</text>
      <text x="36" y="114" text-anchor="middle">-20%</text><text x="86" y="114" text-anchor="middle">0%</text><text x="136" y="114" text-anchor="middle">20%</text><text x="186" y="114" text-anchor="middle">40%</text><text x="236" y="114" text-anchor="middle">60%</text>
      <text x="136" y="124" text-anchor="middle" font-weight="600" fill="#2b8bb8">Growth/Decline</text>
    </g>
    <line x1="86" y1="6" x2="86" y2="106" stroke="#888" stroke-width=".7"/>
    <line x1="36" y1="79" x2="236" y2="79" stroke="#888" stroke-width=".7"/>
    <circle cx="201" cy="22" r="13" fill="#3e4a55"/>
    <text x="201" y="25" font-size="8" fill="#fff" text-anchor="middle" font-family="Barlow,Arial,sans-serif">4</text>
    <text x="218" y="31" font-size="6" fill="#555" font-family="Barlow,Arial,sans-serif">45%</text>
    <circle cx="106" cy="48" r="11" fill="#8fcde6"/>
    <text x="106" y="51" font-size="8" fill="#fff" text-anchor="middle" font-family="Barlow,Arial,sans-serif">3</text>
    <circle cx="96" cy="60" r="12" fill="#2b9bc6"/>
    <text x="96" y="63" font-size="8" fill="#fff" text-anchor="middle" font-family="Barlow,Arial,sans-serif">2</text>
    <circle cx="82" cy="73" r="12" fill="#1c4d78"/>
    <text x="82" y="76" font-size="8" fill="#fff" text-anchor="middle" font-family="Barlow,Arial,sans-serif">1</text>
  </svg>
  <p class="chart-note" style="left:292px;top:421px">Show trends within the portfolio in real time covering premium adequacy and the quality of all business being written.</p>

  <h3 class="section-head" style="left:28px;top:458px">PORTFOLIO EXPOSURE</h3>
  <h3 class="section-head" style="left:290px;top:458px">PREMIUM CHANGE</h3>
  <p class="exposure-note">Report on detailed analyses including sales trend and profitability trends. This allows for a method of managing distribution channels while addressing pricing imbalances.</p>

  <svg class="chart" style="left:22px;top:516px" width="250" height="124" viewBox="0 0 250 124">
    <g font-family="Barlow,Arial,sans-serif" font-size="6.5" fill="#555">
      <text x="30" y="8" text-anchor="end">500</text><text x="30" y="20" text-anchor="end">400</text><text x="30" y="32" text-anchor="end">300</text><text x="30" y="44" text-anchor="end">200</text><text x="30" y="56" text-anchor="end">100</text><text x="30" y="68" text-anchor="end">0</text><text x="30" y="80" text-anchor="end">-100</text><text x="30" y="92" text-anchor="end">-200</text><text x="30" y="104" text-anchor="end">-300</text><text x="30" y="116" text-anchor="end">-400</text>
      <text x="9" y="62" transform="rotate(-90 9 62)" text-anchor="middle" font-weight="600" fill="#2b8bb8">Portfolio Score</text>
    </g>
    <g stroke="#dde3e8" stroke-width=".6">
      <line x1="34" y1="6" x2="240" y2="6"/><line x1="34" y1="18" x2="240" y2="18"/><line x1="34" y1="30" x2="240" y2="30"/><line x1="34" y1="42" x2="240" y2="42"/><line x1="34" y1="54" x2="240" y2="54"/><line x1="34" y1="78" x2="240" y2="78"/><line x1="34" y1="90" x2="240" y2="90"/><line x1="34" y1="102" x2="240" y2="102"/><line x1="34" y1="114" x2="240" y2="114"/>
    </g>
    <line x1="34" y1="66" x2="240" y2="66" stroke="#888" stroke-width=".7"/>
    <polyline fill="none" stroke="#2b8bb8" stroke-width="1.6" points="36,22 44,18 50,24 58,20 64,14 72,22 80,19 88,26 96,20 104,24 112,17 120,23 128,21 136,28 144,24 152,30 160,26 168,32 176,27 184,34 192,30 200,37 208,33 216,40 224,36 232,44 238,41"/>
  </svg>

  <svg class="chart" style="left:286px;top:516px" width="250" height="124" viewBox="0 0 250 124">
    <g font-family="Barlow,Arial,sans-serif" font-size="6.5" fill="#555">
      <text x="34" y="8" text-anchor="end">60%</text><text x="34" y="24" text-anchor="end">40%</text><text x="34" y="40" text-anchor="end">20%</text><text x="34" y="56" text-anchor="end">0%</text><text x="34" y="72" text-anchor="end">-20%</text><text x="34" y="88" text-anchor="end">-40%</text><text x="34" y="104" text-anchor="end">-60%</text>
      <text x="11" y="54" transform="rotate(-90 11 54)" text-anchor="middle" font-weight="600" fill="#2b8bb8">% Change</text>
      <text x="140" y="120" text-anchor="middle" font-weight="600" fill="#2b8bb8">Segment Number</text>
    </g>
    <line x1="38" y1="54" x2="240" y2="54" stroke="#888" stroke-width=".7"/>
    <g fill="#1c4d78">
      <rect x="58" y="54" width="14" height="5"/>
      <rect x="104" y="54" width="14" height="44"/>
      <rect x="150" y="22" width="14" height="32"/>
      <rect x="196" y="36" width="14" height="18"/>
    </g>
    <g font-family="Barlow,Arial,sans-serif" font-size="7" fill="#fff" text-anchor="middle">
      <text x="111" y="72">2</text><text x="157" y="50">3</text><text x="203" y="50">4</text>
    </g>
    <text x="65" y="68" font-family="Barlow,Arial,sans-serif" font-size="7" fill="#555" text-anchor="middle">1</text>
  </svg>

  <footer class="footer">
    <p class="footer-about"><b>Brightfern Metrics</b> provides breakthrough predictive analytics powered by machine learning and the latest statistical techniques, enabling property and casualty insurers to achieve superior performance.</p>
    <div class="brand"><i></i>Brightfern Metrics</div>
    <address class="contact" style="font-style:normal">
      <strong>Brightfern Metrics</strong>, 210 Harlow Avenue<br>
      Suite 400, Ridgeford, SC 29000<br>
      Phone: 555.014.2290 | Fax: 555.014.2291<br>
      <strong>www.brightfernmetrics.com</strong>
    </address>
  </footer>
</section>

</body>
</html>
```